A Recruitment Company Needs a Web Design that Expresses High Energy and Results

Our company, BrightLane Consultants, needs a web design for our recruiting business based in Asia (Taiwan). We provide recruitment services to many international companies. Our client base is as follows:
Hi-Tech - 60%
Healthcare and Consumer/FMCG - 15%
Industrial and Engineering - 15%
Banking and Finance - 10%

The website will be accessed by both clients and job seekers. As such, it should look professional, user-friendly and is interactive.

Sans Serif

add136
ffffff
000000

• Attached is the company's logo. the design mus be in line with it.

```html
<!DOCTYPE html>
<html lang="en">
<head>
<meta charset="utf-8">
<title>BrightLane Consultants – Contact</title>
<link href="https://fonts.googleapis.com/css2?family=Roboto:wght@300;400;500;700&display=swap" rel="stylesheet">
<style>
  :root {
    --brand-green: #add136;
    --ink: #000000;
    --text: #333333;
    --muted: #555555;
    --white: #ffffff;
    --panel: #f0f0f0;
    --field-hint: #b5b5b5;
    --footer: #1b1b1b;
    --map-base: #cfd6c2;
  }
  * { box-sizing: border-box; margin: 0; padding: 0; }
  html, body { width: 1200px; height: 1178px; overflow: hidden; }
  body {
    position: relative;
    background: var(--white);
    font-family: "Roboto", Arial, sans-serif;
    color: var(--text);
  }

  /* Header */
  .site-header {
    position: absolute; left: 0; top: 0; width: 1200px; height: 100px;
    border-bottom: 3px solid var(--brand-green);
  }
  .brand {
    position: absolute; left: 100px; top: 28px;
    display: flex; align-items: center; gap: 10px;
    font-size: 24px; font-weight: 700; color: var(--brand-green);
  }
  .brand-mark { width: 18px; height: 18px; border-radius: 50%; background: var(--brand-green); }
  .header-phone {
    position: absolute; right: 100px; top: 14px;
    font-size: 23px; font-weight: 500; color: #222;
  }
  .main-nav {
    position: absolute; right: 92px; top: 64px;
    display: flex; gap: 0;
  }
  .main-nav a {
    display: block; padding: 0 12px 9px; margin-left: 16px;
    font-size: 13px; color: var(--brand-green); text-decoration: none; letter-spacing: 0.2px;
  }
  .main-nav a.is-active { border-bottom: 3px solid var(--brand-green); }

  /* Page title */
  .page-title {
    position: absolute; top: 132px; width: 1200px; text-align: center;
    font-size: 34px; font-weight: 300; color: #222; letter-spacing: 0.5px;
  }

  /* Intro column */
  .contact-intro { position: absolute; left: 100px; top: 210px; width: 658px; }
  .contact-intro h2 { font-size: 22px; font-weight: 400; color: var(--ink); margin-bottom: 8px; }
  .contact-intro p { font-size: 11px; line-height: 20px; color: var(--muted); margin-bottom: 14px; }
  .address { margin-top: 18px; }
  .address + .address { margin-top: 22px; }
  .address h3 { font-size: 18px; font-weight: 500; color: var(--ink); margin-bottom: 2px; }
  .address li { list-style: none; font-size: 11.5px; line-height: 22px; color: var(--ink); }
  .address a { color: var(--ink); text-decoration: none; }

  /* Form */
  .contact-form {
    position: absolute; left: 783px; top: 212px; width: 319px; height: 391px;
    background: var(--panel); padding: 16px 17px;
  }
  .field {
    display: block; width: 100%; height: 37px; margin-bottom: 13px;
    background: var(--white); border: 0; padding: 0 11px;
    font-family: inherit; font-size: 11px; color: var(--field-hint);
    line-height: 37px;
  }
  .field-message { height: 148px; line-height: 22px; padding-top: 6px; }
  .send-button {
    display: block; width: 100%; height: 42px; border: 0;
    background: var(--brand-green); color: var(--white);
    font-family: inherit; font-size: 14px; font-weight: 700; letter-spacing: 0.5px;
  }

  /* Map */
  .location-map {
    position: absolute; left: 0; top: 643px; width: 1200px; height: 397px;
    background: linear-gradient(135deg, #d6dcc9 0%, var(--map-base) 50%, #c3cdb5 100%);
  }

  /* Footer */
  .site-footer {
    position: absolute; left: 0; top: 1044px; width: 1200px; height: 134px;
    background: var(--footer); border-top: 4px solid #cfcfcf;
  }
  .social-links {
    position: absolute; top: 44px; width: 1200px;
    display: flex; justify-content: center; gap: 32px;
  }
  .social-dot { width: 10px; height: 10px; border-radius: 50%; background: var(--white); }
  .copyright {
    position: absolute; top: 80px; width: 1200px; text-align: center;
    font-size: 12.5px; color: var(--white);
  }
</style>
</head>
<body>
  <header class="site-header">
    <div class="brand"><span class="brand-mark"></span>BrightLane Consultants</div>
    <div class="header-phone">(123) 555 0188</div>
    <nav class="main-nav">
      <a href="#">HOME</a>
      <a href="#">PRODUCTS</a>
      <a href="#">ABOUT US</a>
      <a href="#">OUTSOURCING</a>
      <a href="#" class="is-active">CONTACT US</a>
    </nav>
  </header>

  <h1 class="page-title">Contact-Information</h1>

  <section class="contact-intro">
    <h2>WE WANT TO HEAR FROM YOU</h2>
    <p>We match driven professionals with international companies across Taiwan and Asia. Our consultants work closely with every client to understand the role, the team and the culture before a search begins. Candidates receive honest advice, quick feedback and steady support from first call to signed offer. Whether you are hiring or looking for your next step, tell us what you need and we will reply within one business day.</p>
    <p>Send us a message using the form, call our office, or visit one of our two locations below during regular business hours.</p>

    <div class="address">
      <h3>Address 1</h3>
      <ul>
        <li>Telephone : 1-22-0147</li>
        <li>Fax : 1-22-0148</li>
        <li>Email : <a href="#">hello@brightlane.example</a></li>
      </ul>
    </div>
    <div class="address">
      <h3>Address 2</h3>
      <ul>
        <li>Telephone : 1-22-0147</li>
        <li>Fax : 1-22-0148</li>
        <li>Email : <a href="#">hello@brightlane.example</a></li>
      </ul>
    </div>
  </section>

  <form class="contact-form">
    <div class="field">Your name</div>
    <div class="field">Your email</div>
    <div class="field">Subject</div>
    <div class="field field-message">Message</div>
    <button type="button" class="send-button">SEND</button>
  </form>

  <div class="location-map" role="img" aria-label="Street map showing the office location with a marker"></div>

  <footer class="site-footer">
    <div class="social-links">
      <span class="social-dot"></span>
      <span class="social-dot"></span>
      <span class="social-dot"></span>
      <span class="social-dot"></span>
      <span class="social-dot"></span>
    </div>
    <p class="copyright">Copyright goes here</p>
  </footer>
</body>
</html>
```